Aviation: Overcast Study Guide Book Cover

We need a book cover (front and back) designed for an Instrument Flight Rules (IFR) study guide used by helicopter and airplane pilots to obtain an instrument rating for a helicopter or airplane. Below is the title and subtitles.

TITLE: OVERCAST STUDY GUIDE
SUBTITLE 1: Checkride Preparation for Airplane and Helicopter Pilots
SUBTITLE 2: Prepare for your Instrument Rating with Confidence

We have also upload recommended text to be included on the back cover. In addition, we included images of similar book covers that we like and ones that we do not like. Below are links to two others books by the author.

https://www.bookvarro.example/Rotorcraft-Exam-Handbook-oral-review/dp/507214638K
https://www.bookvarro.example/Manual-Floatwing-Handling-Lionel-Quarrick/dp/5093742816

Flight students

Aviation

• helicopter and airplane

```html
<!DOCTYPE html>
<html lang="en">
<head>
<meta charset="utf-8">
<title>Overcast Study Guide — Cover</title>
<link rel="stylesheet" href="https://fonts.googleapis.com/css2?family=Bebas+Neue&family=Fira+Sans+Condensed:wght@600&family=Montserrat:wght@900&family=Source+Sans+3:ital,wght@0,400;0,600;1,400;1,700&display=swap">
<style>
  :root {
    --sky-top: #e4f1f6;
    --sky-mid: #cfe4ee;
    --sky-deep: #b7d3e2;
    --navy: #0c3a64;
    --royal: #0d5c96;
    --cyan: #1fb6ee;
    --box: #5596e0;
    --spine: #0b5a96;
    --band: rgba(178, 212, 228, 0.75);
    --white: #ffffff;
  }
  * { margin: 0; padding: 0; box-sizing: border-box; }
  html, body { width: 1200px; height: 760px; overflow: hidden; background: var(--white); }
  .cover { position: relative; width: 1200px; height: 760px; overflow: hidden; }

  /* Back cover */
  .back {
    position: absolute; left: 0; top: 0; width: 587px; height: 760px;
    background: radial-gradient(ellipse at 30% 20%, #f4fafc 0%, var(--sky-top) 40%, var(--sky-mid) 100%);
    font-family: "Source Sans 3", sans-serif; color: var(--royal);
  }
  .back-heading {
    position: absolute; left: 57px; top: 66px;
    font-family: "Source Sans 3", sans-serif; font-weight: 600;
    font-size: 17.5px; color: var(--navy); letter-spacing: 0.1px;
  }
  .back-copy { position: absolute; left: 59px; top: 112px; width: 480px; font-size: 12px; line-height: 14px; }
  .back-copy p { margin-bottom: 14px; }
  .back-copy .centered { text-align: center; }
  .topics {
    position: absolute; left: 59px; top: 322px;
    display: grid; grid-template-columns: repeat(3, 144px); grid-auto-rows: 34px;
    column-gap: 11px; row-gap: 8.5px;
  }
  .topic {
    background: var(--box); color: var(--white); font-weight: 600; font-size: 12px;
    display: flex; align-items: center; justify-content: center; white-space: nowrap;
  }
  .about { position: absolute; left: 59px; top: 480px; width: 480px; font-style: italic; font-size: 10px; line-height: 12.6px; }
  .about h2 { font-size: 10.5px; font-weight: 700; color: var(--navy); margin-bottom: 14px; }
  .about p { margin-bottom: 12px; }
  .jet-illustration {
    position: absolute; left: 40px; top: 635px; width: 320px; height: 100px;
    background: radial-gradient(ellipse at 50% 60%, #f3f5f6 0%, #d6e8ea 45%, rgba(110,190,190,0.25) 70%, transparent 80%);
  }
  .isbn-area { position: absolute; left: 431px; top: 662px; width: 139px; height: 83px; background: var(--white); }

  /* Spine */
  .spine {
    position: absolute; left: 587px; top: 0; width: 25px; height: 760px; background: var(--spine);
    color: var(--white);
  }
  .spine-title, .spine-author {
    position: absolute; left: 50%; writing-mode: vertical-rl; transform: translateX(-50%);
    white-space: nowrap;
  }
  .spine-title { top: 36px; font-family: "Montserrat", sans-serif; font-weight: 900; font-size: 13px; letter-spacing: 0.5px; }
  .spine-author { top: 552px; font-family: "Montserrat", sans-serif; font-weight: 900; font-size: 13px; }

  /* Front cover */
  .front {
    position: absolute; left: 612px; top: 0; width: 588px; height: 760px;
    background: linear-gradient(180deg, var(--sky-deep) 0%, var(--sky-mid) 35%, #d6e8ef 60%, var(--sky-mid) 100%);
  }
  .author-band { position: absolute; left: 0; top: 12px; width: 588px; height: 72px; background: var(--band); }
  .author-name {
    position: absolute; left: 0; top: 14px; width: 588px; text-align: center;
    font-family: "Bebas Neue", sans-serif; font-size: 76px; line-height: 70px; color: var(--white);
    letter-spacing: 1px; padding-left: 20px;
  }
  .helicopter-photo {
    position: absolute; left: 118px; top: 62px; width: 380px; height: 165px;
    background: radial-gradient(ellipse at 55% 60%, #f3f5f5 0%, #dfe9ea 35%, rgba(70,150,140,0.35) 58%, transparent 72%);
  }
  .subtitle-band { position: absolute; left: 0; top: 232px; width: 588px; height: 200px; background: rgba(200, 224, 234, 0.35); }
  .subtitle {
    position: absolute; left: 0; width: 588px; text-align: center;
    font-family: "Fira Sans Condensed", sans-serif; font-weight: 600; color: var(--royal); letter-spacing: 0.6px;
  }
  .subtitle-top { top: 237px; font-size: 16.5px; }
  .subtitle-bottom { top: 406px; font-size: 16.5px; }
  .title-art { position: absolute; left: 0; top: 258px; width: 588px; height: 145px; }
  .title-main { font-family: "Montserrat", sans-serif; font-weight: 900; }
  .cockpit-photo {
    position: absolute; left: 0; top: 432px; width: 588px; height: 328px;
    background: linear-gradient(180deg, #3c3f48 0%, #2a2c33 20%, #8ba3b4 32%, #b9cfdc 45%, #3a3d45 62%, #22252b 78%, #2c3a6a 88%, #1c1f25 100%);
  }
</style>
</head>
<body>
<main class="cover">

  <section class="back">
    <h2 class="back-heading">PREPARE FOR YOUR IFR CHECK RIDE WITH CONFIDENCE</h2>
    <div class="back-copy">
      <p>Becoming an instrument rated pilot is one of the most challenging ratings to obtain.<br>
      This guide helps prepare you to pass your IFR check ride with confidence.<br>
      The question-and-answer format is easy to follow and provides detailed explanations for expanded knowledge.</p>
      <p class="centered">Includes Helicopter and Airplane Specific Content</p>
      <p>This guide is designed to prepare an airplane or helicopter pilot the oral portion of the IFR checkride.&nbsp; Unlike other resources, this guide specifically addresses the differences with IFR flight in helicopters.<br>
      As a dual rated pilot, the author ensures to identify areas of differences between the two categories of IFR flight. The following concepts are addressed within the guide.</p>
    </div>

    <div class="topics">
      <div class="topic">• Preflight Actions</div>
      <div class="topic">• Enroute Procedures</div>
      <div class="topic">• Aeromedical Factors</div>
      <div class="topic">• General IFR Concepts</div>
      <div class="topic">• Approach Procedures</div>
      <div class="topic">• WeatherFundamentals</div>
      <div class="topic">• Departure Procedures</div>
      <div class="topic">• IFR Emergences</div>
      <div class="topic">• Risk Management</div>
    </div>

    <div class="about">
      <h2>About the Author:</h2>
      <p>Lionel Quarrick is ATP rated pilot and helicopter and fixed-wing instructor.&nbsp; Lionel is the owner and operator Tailwind Meridian, LLC which does business as Hoverline Aviation and Pelican Float Aviation.&nbsp; Hoverline Aviation provides primary helicopter flight instruction while Pelican Float Aviation provides seaplane flight instruction and tours.</p>
      <p>In addition to instructing, Lionel has authored other books to include The Rotorcraft Exam Handbook, and Manual of Floatwing Handling.&nbsp; Lionel lives in Kentucky with his beautiful wife Marisol.<br>
      They have a daughter, Delia, that is dual rated and employed as a captain for a charter company. Prior to learning to fly, Lionel spent several years in the military as a Special Warfare Combat Craft Crewman in the U.S. Navy and Ranger-qualified infantry officer in the U.S. Army.</p>
    </div>

    <div class="jet-illustration" role="img" aria-label="Illustration of a white business jet with teal tail and wings"></div>
    <div class="isbn-area"></div>
  </section>

  <aside class="spine">
    <span class="spine-title">OVERCAST STUDY GUIDE</span>
    <span class="spine-author">Lionel Quarrick</span>
  </aside>

  <section class="front">
    <div class="author-band"></div>
    <h1 class="author-name">LIONEL QUARRICK</h1>
    <div class="helicopter-photo" role="img" aria-label="Photo of a white and teal twin-engine helicopter in flight"></div>
    <div class="subtitle-band"></div>
    <p class="subtitle subtitle-top">CHECKRIDE PREPARATION FOR AIRPLANE AND HELICOPTER PILOTS</p>

    <svg class="title-art" viewBox="0 0 588 145" aria-label="Overcast Study Guide">
      <text class="title-main" x="294" y="94" text-anchor="middle" font-size="74" textLength="540" lengthAdjust="spacingAndGlyphs"
            fill="#0d5c96" stroke="#1fb6ee" stroke-width="4" paint-order="stroke" stroke-linejoin="round">OVERCAST</text>
      <text class="title-main" x="294" y="138" text-anchor="middle" font-size="38" textLength="332" lengthAdjust="spacingAndGlyphs"
            fill="#0d5c96">STUDY GUIDE</text>
    </svg>

    <p class="subtitle subtitle-bottom">PREPARE FOR YOUR INSTRUMENT RATING WITH CONFIDENCE</p>
    <div class="cockpit-photo" role="img" aria-label="Photo of an airliner cockpit with overhead panel, windscreen and glass instrument displays"></div>
  </section>

</main>
</body>
</html>
```